poster for a contemporary music concert series

Our association is hosting a series of contemporary music concerts.
The setup is classical - from chamber music trio, midsized ensemble until orchestra.
context/topic:
Every ensemble for contemporary music in the city is playing one concert in the series. We have one common topic each year. This year’s topic is about a composition idea  called "Komprovisation". Each concert has one assigned student who is responsible to write a new piece that will be performed. This piece uses material generated by the LAST concert of the series. The used material can be anything (the score, the recording, a video recording, ...).
task:
We need a poster that will be printed in A3 format throughout the city before every concert. The poster must contain all the information of the concert series and must have places for the individual names of the performing ensemble/title/program.
The poster is used six times for six different ensembles. Although it is ONE series, we would like to have it easily visible that there are different concerts. We think the easiest way is to use complete different colors for background to distinguish the different ensembles/program titels from each other.
Things to be included on the poster:
- the title of the concert series is "in:folds".
- the concert place is "Fernwerk-Halle Dresden, großer Saal"
- the price is  "15€ normal / 10€ ermäßigt"
- the logo of TonBogen-Dresden can be used in any of the colours provided - somewhere should be mentioned, that this concert series is a cooperation "in:folds – Eine Konzertreihe von TonBogen-Dresden in Kooperation mit der Fernwerk-Halle Dresden"
- the logo of the museum where we play is included and should be used
- the pdf shows examples of previous years
- there must be one bottom line in white for the needed logos of the funding partners. The funding partners are different from each concert, I included here three of them for visual purposes

Updates
- please don't use parts of the old posters. We have complete new posters for every year. The rectangle and the "Intelligenz" was part of last year's design.
- the music that is coming is not classical in a way that any instrument pictures would help to promote it. It's composed today, so very modern and often with use of electronics (in:folds is often inspired composers to a  kind of feedback, loop, variance, or ... of the previous material)

Target Market(s)
concert audience, young people
Industry/Entity Type
contemporary (classical) music
Requirements
Must have
- things mentioned in the brief description

Nice to have
- a visual look that shows that it is about contemporary music. IF there is any idea how to visualize the IDEA of the concert series this year (taking material from previous concerts and recompose it to the next ensemble) - this would be WONDERFUL. not necessary a copy, nor fake - just a reference to the old ones - and so on :-)

Should not have
- symbolic images/clipart/anything "musically" --> more avantgarde or abstract style is better

```html
<!DOCTYPE html>
<html lang="de">
<head>
<meta charset="utf-8">
<title>in:folds – Konzertreihe</title>
<link rel="stylesheet" href="https://fonts.googleapis.com/css2?family=Oswald:wght@500&family=Poppins:wght@400;500;600&display=swap">
<style>
  :root {
    --poster-dark: #1f0e07;
    --accent: #d9761a;
    --white: #ffffff;
    --footer-ink: #3a3a3a;
    --venue-blue: #1d9fdc;
    --partner-green: #3a9a48;
  }
  * { margin: 0; padding: 0; box-sizing: border-box; }
  html, body { width: 677px; height: 1200px; overflow: hidden; background: var(--white); }
  .poster {
    position: relative; width: 677px; height: 1200px; overflow: hidden;
    background: var(--poster-dark); font-family: "Poppins", sans-serif; color: var(--white);
  }
  .light-trails {
    position: absolute; left: 0; top: 0; width: 677px; height: 660px;
    background:
      radial-gradient(ellipse 260px 160px at 300px 170px, rgba(247,162,28,.85), rgba(247,162,28,0) 70%),
      radial-gradient(ellipse 300px 120px at 560px 80px, rgba(247,162,28,.7), rgba(247,162,28,0) 70%),
      radial-gradient(ellipse 260px 110px at 120px 110px, rgba(200,88,12,.7), rgba(200,88,12,0) 70%),
      linear-gradient(180deg, #7a3208 0%, #4a1d07 35%, var(--poster-dark) 100%);
  }
  .frame {
    position: absolute; left: 30px; top: 420px; width: 616px; height: 592px;
    border-left: 2px solid var(--accent); border-bottom: 2px solid var(--accent);
  }
  .frame-right-top { position: absolute; left: 644px; top: 560px; width: 2px; height: 120px; background: var(--accent); }
  .frame-right-bottom { position: absolute; left: 644px; top: 992px; width: 2px; height: 20px; background: var(--accent); }
  .web {
    position: absolute; left: 645px; top: 840px; transform: translate(-50%, -50%) rotate(-90deg);
    font-size: 15px; white-space: nowrap; letter-spacing: .2px;
  }
  .host {
    position: absolute; left: 104px; top: 376px; display: flex; align-items: center; gap: 10px;
    font-size: 19px; font-weight: 500; letter-spacing: 1px;
  }
  .host-mark { width: 14px; height: 14px; background: var(--white); }
  .series-title {
    position: absolute; left: 100px; top: 396px; font-family: "Oswald", sans-serif; font-weight: 500;
    font-size: 232px; line-height: 1; letter-spacing: -7px; transform: scaleX(.82); transform-origin: left top;
    white-space: nowrap;
  }
  .venue { position: absolute; left: 104px; top: 668px; color: var(--accent); font-weight: 600; font-size: 23px; }
  .prices { position: absolute; left: 104px; top: 726px; display: flex; gap: 40px; }
  .price { display: flex; align-items: center; }
  .price-amount {
    background: var(--accent); border: 2px solid var(--white); font-weight: 600; font-size: 22px;
    padding: 2px 8px; line-height: 1.3;
  }
  .price-label { border: 1.5px solid var(--white); border-left: none; font-weight: 600; font-size: 15px; padding: 3px 10px; }
  .description { position: absolute; left: 104px; top: 806px; font-size: 14.5px; line-height: 1.45; width: 460px; }
  .description em { font-style: normal; color: var(--accent); }
  .program { position: absolute; left: 104px; top: 904px; display: flex; gap: 28px; }
  .program-item { width: 148px; }
  .program-name { color: var(--accent); font-size: 13.5px; text-transform: uppercase; }
  .program-work { font-size: 10.5px; text-transform: uppercase; line-height: 1.45; margin-top: 2px; }
  .partners {
    position: absolute; left: 0; bottom: 0; width: 677px; height: 146px; background: var(--white);
    display: flex; align-items: center; justify-content: center; gap: 34px; color: var(--footer-ink);
  }
  .partner-fund { width: 110px; }
  .partner-fund-head { display: flex; align-items: center; gap: 8px; font-size: 11px; }
  .partner-fund-badge { width: 18px; height: 22px; background: var(--partner-green); }
  .partner-fund-note { font-size: 4.5px; line-height: 1.3; margin-top: 6px; }
  .partner-city { display: flex; align-items: center; gap: 10px; }
  .partner-city-note { font-size: 9.5px; text-align: right; line-height: 1.25; }
  .partner-city-badge { width: 22px; height: 30px; background: var(--footer-ink); }
  .partner-city-name { font-size: 13px; border-left: 1px solid var(--footer-ink); padding-left: 10px; line-height: 2.6; }
  .partner-venue { display: flex; align-items: center; gap: 8px; color: var(--venue-blue); font-weight: 600; font-size: 13px; line-height: 1.1; }
  .partner-venue-dot { width: 42px; height: 42px; border-radius: 50%; background: var(--venue-blue); }
</style>
</head>
<body>
<main class="poster">
  <div class="light-trails" role="img" aria-label="Photo of glowing orange light trails forming a wavy net against a dark background"></div>

  <div class="frame"></div>
  <div class="frame-right-top"></div>
  <div class="frame-right-bottom"></div>
  <p class="web">www.tonbogen-dresden.de</p>

  <div class="host"><span class="host-mark"></span><span>TonBogen Dresden</span></div>
  <h1 class="series-title">in:folds</h1>

  <p class="venue">Fernwerk-Halle Dresden, großer Saal</p>

  <div class="prices">
    <div class="price"><span class="price-amount">15€</span><span class="price-label">Normal</span></div>
    <div class="price"><span class="price-amount">10€</span><span class="price-label">ermäßigt</span></div>
  </div>

  <p class="description"><em>in:folds</em> – Eine Konzertreihe von TonBogen-Dresden in Kooperation mit der Fernwerk-Halle Dresden</p>

  <section class="program">
    <div class="program-item">
      <p class="program-name">Jonas Harlinger:</p>
      <p class="program-work">Pulsfeld Aspect #2</p>
    </div>
    <div class="program-item">
      <p class="program-name">Mirko Stellwag</p>
      <p class="program-work">Auszug aus dem Zyklus<br>Spiegel aus Glut</p>
    </div>
    <div class="program-item">
      <p class="program-name">Ottavo Raum</p>
      <p class="program-work">(Klavier /<br>Live-Elektronik)</p>
    </div>
  </section>

  <footer class="partners">
    <div class="partner-fund">
      <div class="partner-fund-head"><span>Kunstfonds Elbland</span><span class="partner-fund-badge"></span></div>
      <p class="partner-fund-note">Gefördert mit Mitteln des Landes auf Grundlage des Haushalts.</p>
    </div>
    <div class="partner-city">
      <p class="partner-city-note">gefördert durch<br>das Kulturamt<br>der Elbstadt</p>
      <span class="partner-city-badge"></span>
      <span class="partner-city-name">Elbstadt</span>
    </div>
    <div class="partner-venue">
      <span class="partner-venue-dot"></span>
      <span>FERNWERK-HALLE<br>DRESDEN</span>
    </div>
  </footer>
</main>
</body>
</html>
```